The Harvest Ledger App - Modernization & Graphics User Interface Friendliness Updates

We are Harvest Ledger, and we want to bring a new branding look and graphical user interface to the Harvest Ledger App. The app is a quick reference encyclopedia for all things produce. Boasting articles on over 2,000 produce items, with information ranging from taste and application to geographical and cultural significance. Included in its features are over 10 thousand recipes, and the Harvest Ledger App Crop Bazaar – a global initiative to connect farmer, customer, and chef in one sustainable and easy to use application. The design needs to bring a greater sense of social connection – encouraging the user to participate in the 'Crop Bazaar' experience voluntarily. The design should reflect a sense of authority reflecting the authenticity and reliability of the provided information, it's writing, and its sources. Download the App here: hvldg.example/get

Target Market(s)

Women and Men between ages 21-55.

Industry/Entity Type

Education

Font styles to use
Serif
Sans Serif

Colors

Designer to choose colors to be used in the design.

Requirements
Must have
• An updated user interface, the intuitive usability of the app is currently non-existent. We are looking to reflect as the authority on produce. The app design must reflect a professional, user-friendly, up-to-date, and trustworthy feel.
Nice to have
• To incorporate the social draw of the Crop Bazaar we would like to include on the home page "Social Bubbles" (think Pictaloo stories) which updates with shared photos of produce and their location.
Should not have
• An overly complicated theme, distracting or unprofessional colors, and images.

```html
<!DOCTYPE html>
<html lang="en">
<head>
<meta charset="utf-8">
<title>Harvest Ledger – Produce Detail</title>
<link href="https://fonts.googleapis.com/css2?family=Roboto:wght@400;500;700&display=swap" rel="stylesheet">
<style>
  :root {
    --green: #0bb52a;
    --canvas: #111111;
    --screen-bg: #e9edf0;
    --card: #ffffff;
    --ink: #444444;
    --body: #555555;
    --muted: #8a8f94;
    --yellow: #d9b91b;
    --red: #e5161d;
    --divider: #dfe3e6;
  }
  * { box-sizing: border-box; margin: 0; padding: 0; }
  html, body { width: 1200px; height: 1200px; overflow: hidden; background: var(--canvas); }
  body { position: relative; font-family: 'Roboto', Arial, sans-serif; }

  .app-screen {
    position: absolute; left: 274px; top: 19px;
    width: 522px; height: 929px;
    transform: scale(1.25); transform-origin: top left;
    background: var(--screen-bg); overflow: hidden;
  }

  .top-bar { position: absolute; left: 0; top: 0; width: 522px; height: 92px; background: var(--green); color: #fff; box-shadow: 0 1px 3px rgba(0,0,0,.12); }
  .status { position: absolute; top: 9px; left: 0; right: 0; height: 18px; font-size: 15px; }
  .status .carrier { position: absolute; left: 12px; display: flex; align-items: center; gap: 4px; }
  .status .dots { letter-spacing: -1px; font-size: 12px; }
  .status .time { position: absolute; left: 0; right: 0; text-align: center; }
  .status .battery { position: absolute; right: 12px; display: flex; align-items: center; gap: 6px; }
  .battery-cell { width: 32px; height: 12px; border: 1px solid #fff; border-radius: 2px; padding: 1px; position: relative; }
  .battery-cell::before { content: ""; display: block; width: 100%; height: 100%; background: #fff; border-radius: 1px; }
  .battery-cell::after { content: ""; position: absolute; right: -3px; top: 3px; width: 2px; height: 4px; background: #fff; }

  .nav-back { position: absolute; left: 12px; top: 52px; }
  .nav-share { position: absolute; right: 16px; top: 50px; }
  .nav-title { position: absolute; left: 0; right: 0; top: 40px; text-align: center; font-size: 22px; font-weight: 400; }
  .nav-sub { position: absolute; left: 0; right: 0; top: 69px; text-align: center; font-size: 12px; }

  .card { position: absolute; top: 130px; height: 692px; background: var(--card); border-radius: 3px; box-shadow: 0 1px 2px rgba(0,0,0,.06); overflow: hidden; }
  .card-prev { left: -341px; width: 370px; }
  .card-next { left: 493px; width: 370px; }
  .card-main { left: 76px; width: 370px; }
  .card-photo { width: 100%; height: 224px; border-bottom: 1px solid var(--divider); }
  .card-prev .card-photo { background: linear-gradient(180deg, #d8262e 0%, #f2f2f2 45%, #f4f4f4 70%, #d42a45 100%); }
  .card-next .card-photo { background: linear-gradient(180deg, #ffffff 15%, #5f9b3a 35%, #a9d46a 60%, #e0813a 85%, #ffffff 100%); }
  .card-main .card-photo { background: radial-gradient(ellipse at 55% 55%, #e0b22a 0%, #d6a524 40%, #f4f1e6 75%, #ffffff 100%); }

  .produce-name { margin-top: 22px; text-align: center; font-size: 17px; font-weight: 500; color: var(--ink); letter-spacing: .2px; }
  .section { padding: 0 29px; }
  .section-label { font-size: 14px; font-weight: 500; color: var(--ink); }
  .section-text { font-size: 14.5px; line-height: 22px; color: var(--body); margin-top: 13px; }
  .section-desc { margin-top: 34px; }
  .section-taste { margin-top: 22px; }

  .card-actions { position: absolute; left: 0; right: 0; top: 636px; display: flex; justify-content: center; gap: 27px; }
  .action { width: 38px; height: 38px; border-radius: 50%; display: flex; align-items: center; justify-content: center; }
  .action-view { background: var(--yellow); }
  .action-like { background: var(--green); }
  .action-share { background: var(--red); }

  .tab-bar { position: absolute; left: 0; bottom: 0; width: 522px; height: 69px; background: #fff; border-top: 1px solid var(--divider); display: flex; }
  .tab { flex: 1; position: relative; text-align: center; color: var(--muted); }
  .tab-icon { position: absolute; left: 0; right: 0; top: 8px; height: 36px; display: flex; justify-content: center; align-items: center; }
  .tab-label { position: absolute; left: 0; right: 0; top: 52px; font-size: 10px; font-weight: 500; letter-spacing: .2px; }
  .tab-active { color: var(--green); }
  .badge { position: absolute; left: 60px; top: 10px; width: 17px; height: 14px; border-radius: 7px; background: var(--red); color: #fff; font-size: 8px; line-height: 14px; font-weight: 700; }
</style>
</head>
<body>
<main class="app-screen">
  <header class="top-bar">
    <div class="status">
      <div class="carrier"><span class="dots">●●●○○</span> Nordtel
        <svg width="16" height="12" viewBox="0 0 16 12"><path d="M1 4a10 10 0 0 1 14 0M3.5 6.5a6.5 6.5 0 0 1 9 0M6 9a3 3 0 0 1 4 0" fill="none" stroke="#fff" stroke-width="1.6"/><circle cx="8" cy="11" r="1" fill="#fff"/></svg>
      </div>
      <div class="time">4:21 PM</div>
      <div class="battery">
        <svg width="8" height="13" viewBox="0 0 8 13"><path d="M1 3.5l6 5-3 3V1.5l3 3-6 5" fill="none" stroke="#fff" stroke-width="1" opacity=".7"/></svg>
        100% <span class="battery-cell"></span>
      </div>
    </div>
    <svg class="nav-back" width="24" height="18" viewBox="0 0 24 18"><path d="M23 9H2M9 2L2 9l7 7" fill="none" stroke="#fff" stroke-width="2"/></svg>
    <div class="nav-title">Buddhas Hand Citron</div>
    <div class="nav-sub">Last updated Desember 13, 2014</div>
    <svg class="nav-share" width="26" height="26" viewBox="0 0 26 26"><path d="M13 17V2M8 7l5-5 5 5M8 11H3v13h20V11h-5" fill="none" stroke="#fff" stroke-width="1.8"/></svg>
  </header>

  <article class="card card-prev"><div class="card-photo" role="img" aria-label="Photo of strawberries, yogurt and raspberries"></div></article>
  <article class="card card-next"><div class="card-photo" role="img" aria-label="Photo of broccoli, lettuce and carrots"></div></article>

  <article class="card card-main">
    <div class="card-photo" role="img" aria-label="Photo of Buddha's hand citron fruits, one cut open"></div>
    <h1 class="produce-name">BUDDHAS HAND CITRON</h1>
    <section class="section section-desc">
      <h2 class="section-label">DESCRIPTION :</h2>
      <p class="section-text">Lorem ipsum dolor sit amet, consectetur scing elit. Etiam vitae eros efficitur, finibus sapien et, porta libero. Integer facilisis massa dolor. Vi-vamus tempor enim sit amet lectus vehicula, eget luctus quam dignissim. Sed eu accumsan lacus. Nam et ullamcorper magna. Integer id diam varius arcu vestibulum porttitor.</p>
    </section>
    <section class="section section-taste">
      <h2 class="section-label">TASTE :</h2>
      <p class="section-text">Lorem ipsum dolor sit amet, consectetur scing elit. Etiam vitae eros efficitur, finibus sapien et, porta libero. Integer facilisis massa dolor.</p>
    </section>
    <div class="card-actions">
      <span class="action action-view"><svg width="20" height="14" viewBox="0 0 20 14"><path d="M1 7s3.5-6 9-6 9 6 9 6-3.5 6-9 6-9-6-9-6z" fill="none" stroke="#fff" stroke-width="1.8"/><circle cx="10" cy="7" r="2.6" fill="#fff"/></svg></span>
      <span class="action action-like"><svg width="18" height="16" viewBox="0 0 18 16"><path d="M9 15S1 10 1 5a4 4 0 0 1 8-1 4 4 0 0 1 8 1c0 5-8 10-8 10z" fill="#fff"/></svg></span>
      <span class="action action-share"><svg width="16" height="16" viewBox="0 0 16 16"><circle cx="12" cy="3" r="2.4" fill="#fff"/><circle cx="4" cy="8" r="2.4" fill="#fff"/><circle cx="12" cy="13" r="2.4" fill="#fff"/><path d="M12 3L4 8l8 5" fill="none" stroke="#fff" stroke-width="1.6"/></svg></span>
    </div>
  </article>

  <nav class="tab-bar">
    <div class="tab tab-active">
      <div class="tab-icon"><svg width="30" height="34" viewBox="0 0 30 34"><path d="M15 8c-3-2-13-2-13 9 0 8 6 16 9 16 2 0 3-1 4-1s2 1 4 1c3 0 9-8 9-16 0-11-10-11-13-9z" fill="#0bb52a"/><path d="M15 8c0-3 1-5 4-7" stroke="#0bb52a" stroke-width="2" fill="none"/></svg></div>
      <div class="tab-label">PRODUCE</div>
    </div>
    <div class="tab">
      <div class="tab-icon"><svg width="28" height="28" viewBox="0 0 28 28"><circle cx="14" cy="14" r="11" fill="none" stroke="#9aa0a5" stroke-width="1.4"/></svg></div>
      <div class="tab-label">CHIRPLINE</div>
    </div>
    <div class="tab">
      <div class="tab-icon"><svg width="32" height="20" viewBox="0 0 32 20"><path d="M2 10s6-8 14-8 14 8 14 8-6 8-14 8S2 10 2 10z" fill="none" stroke="#9aa0a5" stroke-width="1.4"/><circle cx="16" cy="10" r="4" fill="none" stroke="#9aa0a5" stroke-width="1.4"/></svg></div>
      <span class="badge">42</span>
      <div class="tab-label">SPOTTED</div>
    </div>
    <div class="tab">
      <div class="tab-icon"><svg width="26" height="32" viewBox="0 0 26 32"><rect x="1.5" y="1.5" width="23" height="29" rx="1" fill="none" stroke="#9aa0a5" stroke-width="1.4"/><path d="M4 25h18" stroke="#9aa0a5" stroke-width="1.2"/><path d="M9 15v-4a4 4 0 1 1 8 0v4z" fill="none" stroke="#9aa0a5" stroke-width="1.2"/></svg></div>
      <div class="tab-label">RECIPES</div>
    </div>
    <div class="tab">
      <div class="tab-icon"><svg width="32" height="10" viewBox="0 0 32 10"><circle cx="5" cy="5" r="3.5" fill="none" stroke="#9aa0a5" stroke-width="1.2"/><circle cx="16" cy="5" r="3.5" fill="none" stroke="#9aa0a5" stroke-width="1.2"/><circle cx="27" cy="5" r="3.5" fill="none" stroke="#9aa0a5" stroke-width="1.2"/></svg></div>
      <div class="tab-label">MORE</div>
    </div>
  </nav>
</main>
</body>
</html>
```